Business card for builder specialising in renovations.

Need a card for our building business. Business name is under Martin Pelloe.
Have licence number on card ( 527916K)
Contact number (0400 382 615)
Want to work on logo for some business cards and shirts - something with MP or MPB or open to ideas??
No animations, No hammers. Something sharp and eye catching.
Highlight that we are a renovation specialist. Simple on front with extra details on back with some lines to jot down things.

Target Market(s)

Renovators

Industry/Entity Type

Building

Contact Information for Business Card

2 sided with room on back to jot things down.
Extra details on back so front can be simple ..like, renovations, bathrooms, decks, extensions, new builds,

Logo Text

MP

Font styles to use
Serif

Requirements
Must have
• Eye catching design .
• Name : Martin pelloe
• Licence number
• Contact number - 0400382615
Nice to have
• Some logo design that we can carry through to other forms of advertising
• Local builder
• Quality work
Should not have
• No animations

```html
<!DOCTYPE html>
<html lang="en">
<head>
<meta charset="utf-8">
<title>Martin Pelloe – Business Card</title>
<link rel="stylesheet" href="https://fonts.googleapis.com/css2?family=Montserrat:wght@500;600;700&family=Oswald:wght@500&display=swap">
<style>
  :root {
    --backdrop: #e4e5e7;
    --card-light: #f3f3f3;
    --card-light-tone: #e6e6e6;
    --card-dark: #1a1a1a;
    --blue: #0b9fcc;
    --blue-deep: #0a6fae;
    --blue-text: #2f8fd6;
    --grey: #8c8c8c;
    --grey-light: #c9c9c9;
    --note-line: #5a5a5a;
    --white: #ffffff;
  }
  html, body {
    margin: 0;
    width: 1200px;
    height: 1000px;
    overflow: hidden;
    background: var(--backdrop);
  }
  .stage {
    position: relative;
    width: 1200px;
    height: 1000px;
    display: flex;
    justify-content: center;
    align-items: center;
    gap: 100px;
  }
  .card {
    width: 360px;
    height: 580px;
    display: block;
    box-shadow: 0 10px 30px rgba(0,0,0,0.15);
  }
  .brand-name {
    font-family: "Oswald", sans-serif;
    font-weight: 500;
    font-size: 26px;
    letter-spacing: 1px;
    fill: var(--grey);
  }
  .back-text { font-family: "Montserrat", sans-serif; }
  .back-name { font-size: 25px; font-weight: 700; letter-spacing: 1.5px; }
  .back-name .first { fill: var(--blue-text); }
  .back-name .last { fill: var(--grey-light); }
  .back-phone { font-size: 27px; font-weight: 600; fill: var(--white); letter-spacing: 1px; }
  .back-licence { font-size: 18px; font-weight: 500; fill: var(--grey); }
  .back-licence .num { fill: var(--blue-text); }
  .back-services { font-size: 16px; font-weight: 500; fill: var(--blue-text); }
</style>
</head>
<body>
<main class="stage">

  <!-- Front of card -->
  <svg class="card card-front" viewBox="0 0 360 580" xmlns="http://www.w3.org/2000/svg" aria-label="Front of business card">
    <defs>
      <linearGradient id="front-blue" x1="0" y1="0" x2="1" y2="1">
        <stop offset="0" stop-color="#14b3dd"/>
        <stop offset="1" stop-color="#0a8fc0"/>
      </linearGradient>
      <linearGradient id="front-blue-deep" x1="0" y1="0" x2="0" y2="1">
        <stop offset="0" stop-color="#0a74b5"/>
        <stop offset="1" stop-color="#07568c"/>
      </linearGradient>
      <linearGradient id="front-ground" x1="0" y1="0" x2="1" y2="1">
        <stop offset="0" stop-color="var(--card-light)"/>
        <stop offset="1" stop-color="var(--card-light-tone)"/>
      </linearGradient>
    </defs>
    <rect class="card-ground" width="360" height="580" fill="url(#front-ground)" role="img" aria-label="Light grey background with flowing line pattern"/>
    <rect class="center-band" x="98" y="0" width="164" height="580" fill="var(--card-dark)"/>
    <polygon class="band-top" points="108,0 252,0 252,118 180,158 108,118" fill="url(#front-blue)"/>
    <polygon class="band-chevron-white" points="108,136 180,176 252,136 252,196 180,236 108,196" fill="var(--card-light)"/>
    <polygon class="band-chevron-grey" points="108,214 180,254 252,214 252,254 180,294 108,254" fill="var(--grey)"/>
    <circle class="brand-dot" cx="180" cy="335" r="18" fill="var(--blue-text)"/>
    <text class="brand-name" x="180" y="388" text-anchor="middle" textLength="140" lengthAdjust="spacingAndGlyphs">MARTIN PELLOE</text>
    <polygon class="band-bottom" points="108,580 108,498 180,466 252,498 252,580" fill="url(#front-blue-deep)"/>
  </svg>

  <!-- Back of card -->
  <svg class="card card-back" viewBox="0 0 360 580" xmlns="http://www.w3.org/2000/svg" aria-label="Back of business card">
    <defs>
      <linearGradient id="back-blue" x1="0" y1="0" x2="1" y2="0">
        <stop offset="0" stop-color="#0a86bd"/>
        <stop offset="1" stop-color="#12b5de"/>
      </linearGradient>
    </defs>
    <rect class="card-ground" width="360" height="580" fill="var(--card-dark)"/>
    <polygon class="emblem-frame" points="90,0 270,0 270,250 180,300 90,250" fill="none" stroke="var(--white)" stroke-width="8"/>
    <polygon class="emblem-top" points="102,0 258,0 258,118 180,158 102,118" fill="url(#back-blue)"/>
    <circle class="emblem-dot" cx="180" cy="182" r="16" fill="var(--blue-text)"/>
    <polygon class="emblem-chevron" points="102,204 180,246 258,204 258,236 180,280 102,236" fill="var(--grey)"/>

    <g class="back-text">
      <text class="back-name" x="180" y="355" text-anchor="middle"><tspan class="first">MARTIN</tspan> <tspan class="last">PELLOE</tspan></text>
      <text class="back-phone" x="180" y="392" text-anchor="middle">0400 382 615</text>
      <text class="back-licence" x="180" y="422" text-anchor="middle">Licence number <tspan class="num">527916K</tspan></text>
    </g>

    <rect class="services-band" x="0" y="450" width="360" height="130" fill="var(--white)"/>
    <g class="back-text back-services">
      <text x="180" y="478" text-anchor="middle">Renovation Specialist,</text>
      <text x="180" y="498" text-anchor="middle">Bathrooms, Decks,</text>
      <text x="180" y="518" text-anchor="middle">Extensions, New builds</text>
    </g>
    <rect class="notes-block" x="112" y="532" width="136" height="48" fill="var(--card-dark)"/>
    <g class="notes-lines" stroke="var(--note-line)" stroke-width="1">
      <line x1="122" y1="548" x2="238" y2="548"/>
      <line x1="122" y1="562" x2="238" y2="562"/>
      <line x1="122" y1="576" x2="238" y2="576"/>
    </g>
  </svg>

</main>
</body>
</html>
```